Purple Hair Mask Label For 16oz Jar

Hi!
I need to create a beauty product label with the below details. I've attached some bench mark products sent to me by the customer. Use this for inspiration!
Customer: Harwick, Tovins
Label Size: 11" x 3.25"
Material: glossy finish
Components: 16oz **AMBER** straight side jar w/ smooth *BLACK* cap
Brand: VELOMI (I'm not set on this if you have an idea for something else!)
Product: Color Extending Hair Mask
Main Copy:
--Tone & Repair
--For Perfect Blonde Hair
--Intense Repair Mask
Other Highlights (they like icons; don't have to use all):
--salon formula
--color treated safe
--paraben free
--sulfate free
--phlalate free
--dye-free
--vegan
--no animal testing
--family owned and operated company
--made in Los Angeles, CA
Description: FPO for now
Directions: FPO for now
Caution: FPO for now
Other Copy:
-- 16.9oz / 500mL
--company: Bright Meadow LLC ; Austin, TX 78751 ; brightmeadowgoods.example
--upc: FPO for now
--VELHM16 (sku; small)
Feel free to be creative and use images or whatever you think.
Thank you!
Owen
Look and feel
Each slider illustrates characteristics of the customer's brand and the style your logo design should communicate.

```html
<!DOCTYPE html>
<html lang="en">
<head>
<meta charset="utf-8">
<title>VELOMI Color Extending Hair Mask – Label</title>
<link rel="stylesheet" href="https://fonts.googleapis.com/css2?family=Montserrat:wght@300;400;900&family=Open+Sans:wght@400&family=Oswald:wght@500;600&family=Questrial&display=swap">
<style>
  :root{
    --page:#ffffff;
    --ink:#0b0b0b;
    --gold-dark:#c48a50;
    --gold-mid:#ddb184;
    --gold-light:#f7e4cb;
    --on-ink:#e7c08d;
  }
  *{box-sizing:border-box;margin:0;padding:0}
  html,body{width:1200px;height:1071px;overflow:hidden;background:var(--page)}
  .label{
    position:absolute;left:30px;top:367px;width:1140px;height:337px;
    border:1px solid #b98a5c;
    background:linear-gradient(90deg,var(--gold-dark) 0%,var(--gold-light) 13%,var(--gold-mid) 26%,var(--gold-dark) 36%,var(--gold-light) 47%,var(--gold-mid) 60%,var(--gold-light) 72%,var(--gold-mid) 86%,var(--gold-dark) 100%);
    color:var(--ink);
    font-family:"Open Sans",sans-serif;
  }
  .label > *{position:absolute}
  .section-title{font-family:"Montserrat",sans-serif;font-weight:400;font-size:12.5px;letter-spacing:.2px}
  .small-copy{font-size:8.3px;line-height:10.4px}
  .ingredients-box{left:29px;top:48px;width:220px;border:1px solid var(--ink);border-radius:4px;padding:3px 8px;text-align:justify;font-size:7.4px;line-height:8.6px}
  .directions-copy{left:30px;top:134px;width:210px}
  .direction-list{left:30px;top:196px;list-style:none;font-size:8.3px}
  .direction-list li{height:13.5px;display:flex;align-items:center}
  .direction-list li::before{content:"";width:7px;height:7px;background:var(--ink);margin-right:9px}
  .caution-box{left:30px;top:278px;width:219px;height:31px;background:var(--ink);color:#fff;border-radius:3px;padding:4px 7px;font-size:6.3px;line-height:7px;overflow:hidden}
  .brand-name{left:322px;top:294px;transform-origin:0 0;transform:rotate(-90deg);font-family:"Montserrat",sans-serif;font-weight:900;font-size:48px;line-height:42px;width:265px;letter-spacing:1px}
  .product-type{left:372px;top:294px;transform-origin:0 0;transform:rotate(-90deg);font-family:"Montserrat",sans-serif;font-weight:300;font-size:16.5px;line-height:18px;width:265px;white-space:nowrap}
  .divider{left:408px;top:32px;width:3px;height:264px;background:var(--ink)}
  .headline{left:440px;top:29px;font-family:"Questrial",sans-serif;font-size:34px;line-height:32.5px;font-weight:400;-webkit-text-stroke:.6px var(--ink)}
  .claim{left:440px;display:flex;font-family:"Montserrat",sans-serif;font-weight:400;font-size:18.5px;line-height:19px}
  .claim::before{content:"";width:13px;height:13px;background:var(--ink);margin:3px 9px 0 0;flex:none}
  .claim-repair{top:160px}
  .claim-tone{top:238px}
  .volume{left:688px;top:95px;width:50px;height:33px;background:var(--ink);color:var(--on-ink);font-family:"Oswald",sans-serif;font-weight:500;font-size:11.5px;line-height:14px;text-align:center;padding-top:2px}
  .salon{left:593px;top:141px;width:147px;font-family:"Questrial",sans-serif;font-size:24px;line-height:28px;letter-spacing:16.5px;-webkit-text-stroke:.5px var(--ink)}
  .formula{left:593px;top:172px;width:147px;font-family:"Questrial",sans-serif;font-size:25px;line-height:28px;letter-spacing:.5px;-webkit-text-stroke:.5px var(--ink)}
  .claim-icons{left:594px;top:212px;display:flex;gap:9.5px}
  .claim-icons svg{width:29px;height:29px}
  .company-plate{left:594px;top:259px;width:145px;height:35px;background:var(--ink);color:var(--on-ink);font-family:"Oswald",sans-serif;text-align:center}
  .company-plate .tagline{font-size:7.2px;font-weight:500;line-height:9px;margin-top:5px}
  .company-plate .company{font-size:15.5px;font-weight:600;line-height:18px}
  .about{left:841px;top:27px;width:270px;text-align:center}
  .about .section-title{font-size:9.5px}
  .about-copy{margin-top:6px;font-size:9.3px;line-height:11.5px}
  .producer{left:841px;top:176px;width:270px;text-align:center;font-size:7.5px;line-height:11.5px}
  .producer .gap{margin-top:4px}
  .cruelty-free{left:937px;top:262px;width:30px;height:30px;border-radius:4px;background:linear-gradient(#d7ad80,#c69866)}
  .recycle{left:990px;top:265px;width:24px;height:24px;border-radius:4px;background:linear-gradient(#8e6a45,#4a3826)}
</style>
</head>
<body>
<main class="label">
  <h2 class="section-title" style="left:30px;top:31px">INGREDIENTS</h2>
  <p class="ingredients-box">Nulla, ut, labore dolor dolore culpa ea lorem fugiat amet, consectetur ipsum ad irure. Officia deserunt cillum consectetur aute sint, dolore consectetur ut Nulla, ut, labore dolor dolore culpa ea lorem fugiat amet, consectetur ipsum ad irure. Officia deserunt</p>

  <h2 class="section-title" style="left:30px;top:114px">DIRECTIONS</h2>
  <p class="directions-copy small-copy">Nulla, ut, labore dolor dolore culpa ea lorem fugiat amet, consectetur ipsum ad irure. Officia deserunt cillum consectetur aute sint, dolore consectetur ut deserunt. Lorem fugiat et duis culpa qui lorem sunt. Nisi ut, lorem quis dolor sunt qui reprehenderit.</p>
  <ul class="direction-list">
    <li>LABORE DOLOR DOLORE CULPA</li>
    <li>LABORE DOLOR DOLORE CULPA</li>
    <li>LABORE DOLOR DOLORE CULPA</li>
    <li>LABORE DOLOR DOLORE CULPA</li>
  </ul>

  <h2 class="section-title" style="left:30px;top:261px">CAUTION</h2>
  <p class="caution-box">cillum consectetur aute sint, dolore consectetur ut deserunt. Lorem fugiat et duis culpa qui lorem sunt. Nisi ut, lorem quis dolor sunt qui reprehenderit.</p>

  <h1 class="brand-name">VELOMI</h1>
  <p class="product-type">COLOR EXTENDING HAIR MASK</p>
  <div class="divider"></div>

  <p class="headline">FOR<br>BLONDE<br>HAIR</p>
  <p class="claim claim-repair"><span>INTENSE<br>REPAIR<br>MASK</span></p>
  <p class="claim claim-tone"><span>SAVES<br>TONE OF<br>COLOUR</span></p>

  <p class="volume">16.9oz<br>500mL</p>
  <p class="salon">SALON</p>
  <p class="formula">FORMULA</p>

  <div class="claim-icons" aria-label="Sulphate free, paraben free, vegan, dye free">
    <svg viewBox="0 0 30 30"><circle cx="15" cy="15" r="14" fill="var(--ink)"/><circle cx="15" cy="15" r="7.5" fill="none" stroke="var(--gold-light)" stroke-width="1.2"/><path d="M13 11h4M14 11v4l-3 4h8l-3-4v-4" fill="none" stroke="var(--gold-light)" stroke-width="1.2"/></svg>
    <svg viewBox="0 0 30 30"><circle cx="15" cy="15" r="14" fill="var(--ink)"/><circle cx="15" cy="15" r="7.5" fill="none" stroke="var(--gold-light)" stroke-width="1.2"/><path d="M11 18l3-3 2 2 3-5" fill="none" stroke="var(--gold-light)" stroke-width="1.2"/></svg>
    <svg viewBox="0 0 30 30"><circle cx="15" cy="15" r="14" fill="var(--ink)"/><circle cx="15" cy="15" r="8" fill="var(--gold-light)"/><path d="M11 19c0-5 3-8 8-8 0 5-3 8-8 8zM11 19l5-5" fill="var(--ink)" stroke="var(--ink)" stroke-width=".8"/></svg>
    <svg viewBox="0 0 30 30"><circle cx="15" cy="15" r="14" fill="var(--ink)"/><circle cx="15" cy="15" r="8" fill="var(--gold-light)"/><path d="M12 18l5-5 2 2-5 5h-2z" fill="var(--ink)"/></svg>
  </div>

  <div class="company-plate">
    <p class="tagline">FAMILY OWNED AND OPERATED COMPANY</p>
    <p class="company">BRIGHT MEADOW LLC</p>
  </div>

  <section class="about">
    <h2 class="section-title">ABOUT THE PRODUCT</h2>
    <p class="about-copy">Nulla, ut, labore dolor dolore culpa ea lorem fugiat amet, consectetur ipsum ad irure. Officia deserunt cillum consectetur aute sint, dolore consectetur ut deserunt. Lorem fugiat et duis culpa qui lorem sunt. Nisi ut, lorem quis dolor sunt qui reprehenderit. Ea amet fugiat, officia commodo est minim ea deserunt voluptate nulla ad excepteur in laboris pariatur excepteur. Fugiat elit est sit elit. Ad eu ut elit, do, ut quis amet consectetur veniam in ea nulla elit. Ut esse qui non et pariatur consectetur eiusmod, irure, lorem, occaecat reprehenderit non et nisi sint. Est anim enim nulla.</p>
  </section>

  <div class="producer">
    <p>Produced by:</p>
    <p>BRIGHT MEADOW LLC</p>
    <p>FAMILY OWNED AND OPERATED COMPANY</p>
    <p class="gap">&#9679; Austin, TX 78751</p>
    <p>brightmeadowgoods.example</p>
    <p>MADE IN LOS ANGELES, CA</p>
  </div>

  <div class="cruelty-free" role="img" aria-label="Not tested on animals symbol"></div>
  <div class="recycle" role="img" aria-label="Recycling symbol"></div>
</main>
</body>
</html>
```